Flyer for an pediatric sleep consultancy - to distribute to play and childcare centers etc.

I need a flyer that will attract the attention of parents with children between the age of babies to toddlers, who may be experiencing sleep issues. The flyer will be placed at places such as community centers, doctors room, play centers, kindergardens, etc.

My company is called "The Quiet Meadow Studio" and provides a sleep consultancy service. My service essentially provides a customized plan for parents to follow and general advice and guidance. It is not medical advice.

I like to the flyer to have an overall tone that is soft and peaceful with a clean and beautiful design, however can catch the attention of parents who may be struggling with their child's sleep issues and are sleep deprived. I would like photos with minimal text. The colour I use is a brownish rose. I will attach some of my designs to give you an idea. You can have a look at my homepage as well to get an idea about my esthetic direction and the colour. Although the colour of my page is a bit too brownish....

I will provide the text to appear in the flyer once I have a better idea of the layout that I prefer for the flyer. The text however wont be extensive, just some catchy points.

I want to direct people to my website which is www.quietmeadowstudio-example.com
I offer a first FREE evaluation call, to the parents, to get to know each other better, learn about their child's particular sleep problems and see if we are a good fit and can work together. I would like to have this information somehow on the flyer, so that the parents will contact me.
I also have a facebook page, which is: The Quiet Meadow Studio

I have a logo that I would like to appear on the flyer. I will attach the file once the uploader on art bazaar is fixed.

When I print the flyer - I like to print A5 SIZE ... please make sure the formatting is OK for this size.

Here are some text ideas. of course all of it would be too much, I guess. On the front of the flyer I would like to have some catchy phrase or something similar to get people interested and to want to know more. On the back there could be a bit more text and information. But I'm open too suggestions....
I'm not too sure about the wording yet. But here are some text that I might be use:

Is sleep an issue in your home?

Is your baby having trouble sleeping? ... are you?!
I can help!

Sleep, baby, sleep….

Teaching children how to sleep

The Quiet Meadow Studio is a pediatric sleep consultancy that specializes in helping parents with children who struggle to develop good and healthy sleep habits.
Disruptive sleep patterns or not enough sleep can affect the physical, mental and emotional development of your child.

Of course nobody plans to have a sleep problem, but habits can become easily ingrained and spiral quickly out of control and you can find yourself sleep deprived, desperate and not too sure what to do. You see all the other sleeping babies and wish there was someone who understood what you were going through?! Well, there is!

Contact me for a free 15 minute consultation.

This 15 minute „mini“ consultation is a chance to discuss your unique sleep challenges and sleep goals with me. I will provide you with an overview of how I will work with your family to achieve your wildest sleep dreams (goals).
Furthermore do I understand and believe that every child and their family is unique and there is no one size fits all!
I would love to have a chat with you and talk about how I can help make things easier for you and your family!

Do I need a sleep consultant for my child?
The answer is yes if:
- if your child will only fall asleep when nursing or bottle feeding
- if your child needs a dummy or other external aid, like being rocked, patted or taken for a care ride to fall asleep
- if your good night routine is a challenging and exhausting procedure instead of a relaxed and enjoyable moment for the whole family
- if sleep is a constant battle in your home which leaves you feeling frustrated and exhausted
- if your own lack of sleep is taking a toll on you and the whole family

What can I do for you?

I will:

- Guide you to set an age appropriate foundation for good sleep
- Create an individual sleep plan tailored especially to your child’s sleep needs and circumstances
- Help you to teach your childto go to sleep and get back to sleep independently during the night
- show you how to teach your child to take healthful, restorative naps
-Learn

Contact:

Marta Lindqvist
info@quietmeadowstudio-example.com
www.quietmeadowstudio-example.com
+34 612 380 574

Consultations in English, German or Spanish via Phone/video call or home consultation

Reason: I have to go on a business trip and won't be able to choose a design until the deadline. During the trip I won't have time to give feedback and ask for changes. thank you

Target Market(s)

parents, sleep deprived mothers, young families, child care provider,

Industry/Entity Type

Baby Care

Contact Information for Business Card

Marta Lindqvist
pediatric sleep consultant
+34 612 380 574

```html
<!DOCTYPE html>
<html lang="en">
<head>
<meta charset="utf-8">
<title>The Quiet Meadow Studio – Flyer</title>
<link href="https://fonts.googleapis.com/css2?family=Tinos:wght@400;700&display=swap" rel="stylesheet">
<style>
  :root {
    --rose: #f1a89c;
    --rose-text: #f0998a;
    --rose-pale: #fde3dd;
    --grey-text: #6f7876;
    --ink: #2f2f2f;
    --sage: #82948e;
    --paper: #ffffff;
    --backdrop: #e9e7e6;
    --photo-skin: #f2d6c8;
    --photo-hair: #c9a27c;
  }
  * { margin: 0; padding: 0; box-sizing: border-box; }
  html, body { width: 1200px; height: 844px; overflow: hidden; }
  body {
    background: var(--backdrop);
    font-family: "Tinos", "Times New Roman", serif;
    position: relative;
  }
  .page {
    position: absolute;
    top: 66px;
    width: 501px;
    height: 711px;
    background: var(--paper);
    overflow: hidden;
  }
  .page--front { left: 83px; }
  .page--back { left: 615px; }

  /* Front */
  .brand-name {
    position: absolute; top: 82px; left: 0; width: 100%;
    text-align: center; font-size: 24px; color: var(--grey-text);
    display: flex; justify-content: center; align-items: center; gap: 10px;
  }
  .brand-dot { width: 10px; height: 10px; border-radius: 50%; background: var(--rose); }
  .cover-photo {
    position: absolute; top: 216px; left: 0; width: 100%; height: 495px;
    background:
      radial-gradient(ellipse 45% 38% at 50% 48%, var(--photo-skin) 0%, rgba(242,214,200,0.6) 55%, rgba(255,255,255,0) 100%),
      radial-gradient(ellipse 40% 25% at 58% 20%, rgba(201,162,124,0.55) 0%, rgba(255,255,255,0) 100%),
      linear-gradient(180deg, #ffffff 0%, #f6f2f0 40%, #f4efec 75%, #ffffff 100%);
  }
  .headline {
    position: absolute; top: 162px; left: 0; width: 100%;
    display: flex; justify-content: center; align-items: center; gap: 6px;
    font-size: 41px; color: var(--rose-text); letter-spacing: 0.5px;
  }
  .headline-rule { width: 37px; height: 1px; background: var(--rose-text); }
  .tagline {
    position: absolute; top: 201px; left: 0; width: 100%;
    text-align: center; font-size: 20px; color: var(--grey-text);
  }
  .web-badge {
    position: absolute; left: 135px; top: 666px; width: 231px; height: 30px;
    border: 1px solid var(--rose); border-radius: 3px; background: rgba(255,255,255,0.85);
    display: flex; justify-content: center; align-items: center;
    font-size: 14px; color: var(--grey-text);
  }

  /* Back */
  .intro {
    position: absolute; top: 40px; left: 16px; width: 470px;
    font-size: 10px; line-height: 12px; color: var(--ink);
  }
  .intro p + p { margin-top: 12px; }
  .offer-band {
    position: absolute; top: 156px; left: 0; width: 100%; height: 160px;
    background: var(--rose);
  }
  .offer-title {
    position: absolute; top: 13px; left: 55px; width: 396px; height: 26px;
    border: 1px solid #fff; color: #fff;
    display: flex; justify-content: center; align-items: center;
    font-size: 18px; font-weight: 700; letter-spacing: 0.2px;
  }
  .offer-text {
    position: absolute; top: 56px; left: 16px; width: 470px;
    font-size: 10px; line-height: 12px; color: var(--rose-pale);
  }
  .column {
    position: absolute; top: 351px; font-size: 10px; line-height: 12px; color: var(--ink);
  }
  .column--needs { left: 18px; width: 225px; }
  .column--offer { left: 261px; width: 222px; }
  .column-divider {
    position: absolute; left: 250px; top: 347px; width: 1px; height: 249px;
    background: #e7c9c3;
  }
  .column-heading {
    font-size: 11px; font-weight: 700; color: var(--rose-text); line-height: 14px;
    margin-bottom: 10px;
  }
  .checklist { list-style: none; }
  .checklist li { position: relative; padding-left: 13px; margin-bottom: 12px; }
  .checklist li::before {
    content: ""; position: absolute; left: 0; top: 3px;
    width: 5px; height: 5px; border-radius: 50%; background: var(--rose);
  }
  .footer-shape { position: absolute; left: 0; top: 597px; width: 501px; height: 114px; }
  .contact-name {
    position: absolute; left: 17px; top: 632px; font-size: 28px; color: #fff;
  }
  .contact-languages {
    position: absolute; left: 17px; top: 669px; width: 210px;
    font-size: 9.5px; line-height: 12px; color: var(--rose-pale);
  }
  .contact-lines {
    position: absolute; left: 276px; top: 638px; list-style: none;
    font-size: 12.5px; line-height: 17px; color: #fff;
  }
  .contact-lines li { display: flex; align-items: center; gap: 6px; }
  .contact-lines svg { width: 11px; height: 11px; flex: none; }
</style>
</head>
<body>

<section class="page page--front">
  <div class="cover-photo" role="img" aria-label="Photograph of a young child sleeping peacefully on a white pillow"></div>
  <div class="brand-name"><span class="brand-dot"></span>The Quiet Meadow Studio</div>
  <h1 class="headline"><span class="headline-rule"></span>SLEEP BABY SLEEP<span class="headline-rule"></span></h1>
  <p class="tagline">Teaching children how to sleep</p>
  <div class="web-badge">www.quietmeadowstudio-example.com</div>
</section>

<section class="page page--back">
  <div class="intro">
    <p>The Quiet Meadow Studio is a pediatric sleep consultancy that specializes in helping parents with children who struggle to develop good and healthy sleep habits.<br>Disruptive sleep patterns or not enough sleep can affect the physical, mental and emotional development of your child.</p>
    <p>Of course nobody plans to have a sleep problem, but habits can become easily ingrained and spiral quickly out of control and you can find yourself sleep deprived, desperate and not too sure what to do. You see all the other sleeping babies and wish there was someone who understood what you were going through?! Well, there is!</p>
  </div>

  <div class="offer-band">
    <h2 class="offer-title">Contact me for a free 15 minute consultation</h2>
    <p class="offer-text">This 15 minute „mini“ consultation is a chance to discuss your unique sleep challenges and sleep goals with me. I will provide you with an overview of how I will work with your family to achieve your wildest sleep dreams (goals).<br>Furthermore do I understand and believe that every child and their family is unique and there is no one size fits all!<br>I would love to have a chat with you and talk about how I can help make things easier for you and your family!</p>
  </div>

  <div class="column column--needs">
    <h3 class="column-heading">Do I need a sleep consultant for my child?<br>The answer is yes if:</h3>
    <ul class="checklist">
      <li>if your child will only fall asleep when nursing or bottle feeding</li>
      <li>if your child needs a dummy or other external aid, like being rocked, patted or taken for a care ride to fall asleep</li>
      <li>if your good night routine is a challenging and exhausting procedure instead of a relaxed and enjoyable moment for the whole family</li>
      <li>if sleep is a constant battle in your home which leaves you feeling frustrated and exhausted</li>
      <li>if your own lack of sleep is taking a toll on you and the whole family</li>
    </ul>
  </div>
  <div class="column-divider"></div>
  <div class="column column--offer">
    <h3 class="column-heading">What can I do for you?<br>I will:</h3>
    <ul class="checklist">
      <li>Guide you to set an age appropriate foundation for good sleep</li>
      <li>Create an individual sleep plan tailored especially to your child’s sleep needs and circumstances</li>
      <li>Help you to teach your childto go to sleep and get back to sleep independently during the night</li>
      <li>show you how to teach your child to take healthful, restorative naps</li>
      <li>Learn</li>
    </ul>
  </div>

  <svg class="footer-shape" viewBox="0 0 501 114" preserveAspectRatio="none" aria-hidden="true">
    <path d="M0 26 Q230 -8 501 26 L501 34 Q230 4 0 36 Z" fill="var(--sage)"/>
    <path d="M0 36 Q230 4 501 34 L501 114 L0 114 Z" fill="var(--rose)"/>
  </svg>
  <div class="contact-name">Marta Lindqvist</div>
  <p class="contact-languages">Consultations in English, German or Spanish via Phone/video call or home consultation</p>
  <ul class="contact-lines">
    <li><svg viewBox="0 0 12 12"><circle cx="6" cy="6" r="5.3" fill="none" stroke="#fff"/><rect x="3" y="4" width="6" height="4" fill="none" stroke="#fff" stroke-width="0.8"/></svg>info@quietmeadowstudio-example.com</li>
    <li><svg viewBox="0 0 12 12"><circle cx="6" cy="6" r="5.3" fill="none" stroke="#fff"/><ellipse cx="6" cy="6" rx="2.2" ry="5" fill="none" stroke="#fff" stroke-width="0.7"/><line x1="1" y1="6" x2="11" y2="6" stroke="#fff" stroke-width="0.7"/></svg>www.quietmeadowstudio-example.com</li>
    <li><svg viewBox="0 0 12 12"><circle cx="6" cy="6" r="5.3" fill="none" stroke="#fff"/><path d="M4 3.5 L5 3.5 L5.5 5 L4.8 5.6 Q5.5 7 6.6 7.4 L7.2 6.7 L8.5 7.2 L8.5 8.3 Q5.5 8.6 3.8 4.5 Z" fill="#fff"/></svg>+34 612 380 574</li>
  </ul>
</section>

</body>
</html>
```